Bus Card for Organic Hydroponic Produce company

We need a business card for a budding new business. We grow 100% organic, 100% hydroponic, 100% GMO free produce for sale in our local area. We need something bold and dynamic, not simple and elegant. We want to catch peoples attention and get them to visit our website to view more information about our products and services. Its difficult to explain on a business card the differences between our produce (tomatoes, cucumbers, peppers, etc...) and the kind they would buy at the local grocer or market. , so we need to push them to the website.
We have been brainstorming names for the company and have a few in mind, so choose whichever speaks most to your artistic flair and propose a card based on that one, or both. #1 "Tressel Organics" with a slogan something like....." When merely growing greens merely won't do the job" OR #2 "Quorvane Organics" with a slogan similar to...."The cutting edge in cleaner, purer organics" OR #3" "Harbrook Organics" with a slogan similar to: "Building a healthier future for those we leave behind"" OR #4 "Weltam Furrow" with a slogan similar to: "Purity by Simplicity"
Eventually we will need assistance with web design, promotional and sales materials, etc. so if you offer those services, please indicate that with the design, though it is NOT necessary to offer any additional services to win this contest. WE will pick the winner solely on the business card we like the most.
We want something that stands out, and especially with the name "Tilda's organics", we understand that a creative mind may wander into certain attention getting means that may not be quite within the realm of what we can hand out at our local grocer or farmers market. We definitely are not opposed to a little salacious undertone or allusion to attract attention, but please keep it tasteful if you skirt that grey area.
For our card, we use an online printer that can add foils, special die cuts, double sided cards, 3-d cards (we love these 32 pt cards), transparent or translucent cards and more. We love cards that have some of these things where possible and on all of our other business' cards we get rave reviews from customers about their uniqueness. brindlepress.example has the info on these accents if you wish to view what I am referencing.
So in conclusion, we want a unique, stylish, bold, vivid, 2 sided business card that will really stand out. Just usw a generic phone number and website for now and we will add them as they become available. Please email with any questions! Thanks in advance for your effort and creativity!
Target Market(s)
We are targeting parents who are conceintous of what their children and families are eating. Our target audience are moms, but we don't want to exclude anyone else who chooses to eat more healthy. Our target customer is the same customer that would shop at Marrowby Grain stores or local farmers markets

```html
<!DOCTYPE html>
<html lang="en">
<head>
<meta charset="utf-8">
<title>Tilda's organics – Business Card</title>
<link rel="stylesheet" href="https://fonts.googleapis.com/css2?family=Arimo:wght@400;700&display=swap">
<style>
  :root {
    --green-deep: #4f8f27;
    --green-mid: #6fae2e;
    --green-bright: #a8d13c;
    --paper: #ffffff;
    --ink-grey: #555a55;
    --backdrop: #e9ebe6;
    --divider: #6aa42f;
  }
  * { box-sizing: border-box; margin: 0; padding: 0; }
  html, body {
    width: 1200px; height: 1000px; overflow: hidden;
    background: var(--backdrop);
    font-family: "Arimo", Arial, sans-serif;
  }
  .canvas { position: relative; width: 1200px; height: 1000px; }
  .card {
    position: absolute; left: 220px; width: 760px; height: 434px;
    border-radius: 28px; overflow: hidden; background: var(--paper);
    box-shadow: 0 6px 18px rgba(0,0,0,0.12);
  }
  .card-front { top: 50px; }
  .card-back { top: 516px; }
  .card-art { position: absolute; inset: 0; width: 760px; height: 434px; }

  .front-name {
    position: absolute; left: 0; right: 0; top: 150px;
    text-align: center; color: var(--paper);
    font-size: 66px; font-weight: 400; letter-spacing: 1px;
  }
  .front-slogan {
    position: absolute; left: 0; right: 0; top: 372px;
    text-align: center; color: var(--ink-grey);
    font-size: 22px; letter-spacing: 0.5px;
  }

  .back-name {
    position: absolute; left: 42px; top: 92px; width: 260px;
    color: var(--green-mid); font-size: 46px; font-weight: 700; line-height: 1.05;
  }
  .back-divider {
    position: absolute; left: 318px; top: 38px; width: 2px; height: 200px;
    background: var(--divider);
  }
  .contact-list { position: absolute; left: 342px; top: 52px; list-style: none; }
  .contact-item {
    display: flex; align-items: center; gap: 14px;
    color: var(--ink-grey); font-size: 20px; line-height: 1.2;
    margin-bottom: 18px;
  }
  .contact-icon { width: 32px; height: 32px; flex: none; }
  .website {
    position: absolute; left: 0; right: 0; bottom: 62px;
    text-align: center; color: var(--paper);
    font-size: 40px; font-weight: 700; letter-spacing: 0.5px;
  }
</style>
</head>
<body>
<main class="canvas">

  <section class="card card-front" aria-label="Card front">
    <svg class="card-art" viewBox="0 0 760 434" aria-hidden="true">
      <defs>
        <radialGradient id="frontGlow" cx="0.55" cy="0.35" r="0.75">
          <stop offset="0" stop-color="#a8d13c"/>
          <stop offset="1" stop-color="#4f8f27"/>
        </radialGradient>
      </defs>
      <path d="M0 0 H760 V300 Q380 330 0 352 Z" fill="url(#frontGlow)"/>
    </svg>
    <h1 class="front-name">Tilda's organics</h1>
    <p class="front-slogan">" As pure as if it were picked at first light"</p>
  </section>

  <section class="card card-back" aria-label="Card back">
    <svg class="card-art" viewBox="0 0 760 434" aria-hidden="true">
      <defs>
        <linearGradient id="bandGlow" x1="0" y1="0" x2="1" y2="0">
          <stop offset="0" stop-color="#4f8f27"/>
          <stop offset="0.6" stop-color="#a8d13c"/>
          <stop offset="1" stop-color="#5e9e2b"/>
        </linearGradient>
      </defs>
      <path d="M0 300 Q380 250 760 196 V434 H0 Z" fill="url(#bandGlow)"/>
    </svg>
    <h2 class="back-name">Tilda's organics</h2>
    <div class="back-divider"></div>
    <ul class="contact-list">
      <li class="contact-item">
        <svg class="contact-icon" viewBox="0 0 32 32" aria-hidden="true">
          <circle cx="16" cy="16" r="15" fill="#6fae2e"/>
          <path d="M11 9 l3 0 1.5 4 -2 1.5 q1.5 3 4 4.5 l1.5-2 4 1.5 0 3 q-1 1.5-3 1.5 q-9-1-11-11 q0-2 2-3z" fill="#fff"/>
        </svg>
        <span>555-014-2288</span>
      </li>
      <li class="contact-item">
        <svg class="contact-icon" viewBox="0 0 32 32" aria-hidden="true">
          <circle cx="16" cy="16" r="15" fill="#6fae2e"/>
          <rect x="8" y="10" width="16" height="12" rx="1" fill="#fff"/>
          <path d="M8 10 L16 17 L24 10" fill="none" stroke="#6fae2e" stroke-width="1.5"/>
        </svg>
        <span>tildasorganics@mailbox.example</span>
      </li>
      <li class="contact-item">
        <svg class="contact-icon" viewBox="0 0 32 32" aria-hidden="true">
          <circle cx="16" cy="16" r="15" fill="#6fae2e"/>
          <path d="M16 7 a6 6 0 0 1 6 6 c0 5-6 12-6 12 s-6-7-6-12 a6 6 0 0 1 6-6z" fill="#fff"/>
          <circle cx="16" cy="13" r="2.3" fill="#6fae2e"/>
        </svg>
        <span>48 Orchard Lane,<br>Fenwick Bay, VA 23499</span>
      </li>
    </ul>
    <p class="website">www.TildasOrganics.example</p>
  </section>

</main>
</body>
</html>
```